Cadenza Elite Keyboard Academy is a comprehensive piano studio located in CBD area and provide individual piano lessons.

We also provide services for wedding organising band, or instrumental hiring or venue hiring, or organise concert to students.

I want my name card to be very creative, does not have to be the form or shape with the normal name card, can be in different shape. Also, I want the name card to be very upper class, because learning piano is a serious thing, so I do not want people to bargain with the prices. I want people to see it as a very elegant tuition so that they do not want to bargain and think it is worth to try.

Further more, Cadenza Elite Keyboard Academy is not like normal piano studio only provide piano lessons, we provide band services for each other event, such as cruise party, wedding etc. I want people to see it as owner of Elite Keyboard Academy, they will have different type of services all in one, I provide more than that, and I am well connected. I do not provide only piano lesson, but also all other musical knowledge and I am very professional

I want name card to be very simple, just name of company name, my name and website that's all, maybe phone number and email as well.

Please check my website to have more ideal concept.
http://harrietdowse.sitebuilder-example.com/cadenzakeyboard
Updates

Target Market(s)

For all people who love to play piano (better with upper class)

Industry/Entity Type

Wedding

Contact Information for Business Card

Harriet Dowse
Mobile:0418769052
Email: cadenzaelitekeys@mailbox-example.com

Colors

Designer to choose colors to be used in the design.

Requirements
Must have
• Creativity
Nice to have
• Black and white
some sort of piano image
Should not have
• Childish

```html
<!DOCTYPE html>
<html lang="en">
<head>
<meta charset="utf-8">
<title>Cadenza Elite Keyboard Academy – Business Card</title>
<link href="https://fonts.googleapis.com/css2?family=Arimo:wght@700&family=Questrial&family=Open+Sans:wght@400&display=swap" rel="stylesheet">
<style>
  :root {
    --backdrop: #bccbd8;
    --card-grey: #d3d3d3;
    --ink: #1a1a1a;
    --band-dark: #1b1c1e;
    --accent-red: #e3173a;
    --paper: #ffffff;
    --light-text: #f2f2f2;
  }
  * { margin: 0; padding: 0; box-sizing: border-box; }
  html, body { width: 1200px; height: 1000px; overflow: hidden; }
  body {
    background: linear-gradient(160deg, #b5c6d5 0%, var(--backdrop) 60%, #c6d3de 100%);
    position: relative;
    font-family: "Questrial", sans-serif;
  }
  .card { position: absolute; left: 281px; width: 654px; overflow: hidden; }

  /* Front card */
  .card-front { top: 79px; height: 374px; background: var(--card-grey); }
  .front-company {
    position: absolute; left: 9px; top: 168px;
    font-family: "Arimo", sans-serif; font-weight: 700; font-size: 17px;
    color: var(--ink); letter-spacing: 0.3px;
  }
  .front-role {
    position: absolute; right: 81px; top: 139px;
    font-size: 18px; color: var(--accent-red);
  }
  .front-name {
    position: absolute; right: 26px; top: 160px;
    font-size: 30px; color: var(--ink);
  }
  .front-rule { position: absolute; left: 0; top: 209px; width: 100%; height: 3px; background: #9a9a9a; }
  .contact-band {
    position: absolute; left: 0; top: 212px; width: 100%; height: 134px;
    background: var(--band-dark);
  }
  .contact-item {
    position: absolute; display: flex; align-items: center; gap: 10px;
    font-family: "Open Sans", sans-serif; font-size: 13px; color: var(--light-text);
  }
  .contact-item svg { flex: none; }
  .contact-phone { left: 36px; top: 36px; }
  .contact-email { left: 36px; top: 83px; }
  .contact-web { left: 318px; top: 58px; font-size: 11.5px; }
  .front-foot { position: absolute; left: 0; top: 346px; width: 100%; height: 15px; background: var(--paper); }

  /* Back card */
  .card-back { top: 515px; height: 375px; background: var(--card-grey); }
  .keyboard-photo {
    position: absolute; left: 0; top: 0; width: 100%; height: 147px;
    background: linear-gradient(180deg, #6f6e6a 0%, #2b2b2d 40%, #1d1d1f 62%, #d9d6cf 78%, #8d8a86 100%);
  }
  .red-rail {
    position: absolute; left: 37px; top: 137px; width: 588px; height: 14px;
    background: var(--accent-red); border-radius: 7px 7px 0 0;
  }
  .name-panel {
    position: absolute; left: 0; top: 147px; width: 329px; height: 83px;
    background: var(--paper);
  }
  .name-panel-extend { position: absolute; left: 329px; top: 147px; width: 325px; height: 28px; background: var(--paper); }
  .brand-name {
    position: absolute; left: 31px; top: 24px;
    font-size: 29px; color: var(--ink); letter-spacing: 0.5px;
    display: flex; align-items: center; gap: 10px;
  }
  .brand-square { width: 14px; height: 14px; background: var(--ink); }
  .service-tab {
    position: absolute; left: 338px; top: 175px; width: 277px; height: 47px;
    background: var(--accent-red);
    clip-path: polygon(14px 0, 100% 0, calc(100% - 14px) 100%, 0 100%);
    border-radius: 0 0 0 6px;
    display: flex; align-items: center; padding-left: 20px;
    font-family: "Arimo", sans-serif; font-weight: 700; font-size: 12.5px; color: var(--paper);
  }
  .venue-photo {
    position: absolute; left: 0; top: 230px; width: 327px; height: 145px;
    background: linear-gradient(135deg, #1b2a6a 0%, #3848b8 35%, #a2243c 60%, #2a3a8c 85%, #121a44 100%);
  }
  .service-list {
    position: absolute; left: 357px; top: 231px; list-style: none;
  }
  .service-list li {
    display: flex; align-items: center; gap: 13px;
    height: 29.3px; font-size: 16px; color: var(--ink);
  }
  .service-list li::before {
    content: ""; width: 13px; height: 13px; border-radius: 50%;
    background: var(--accent-red); border: 2.5px solid var(--band-dark);
  }
</style>
</head>
<body>

<section class="card card-front" aria-label="Business card front">
  <h1 class="front-company">CADENZA ELITE KEYBOARD ACADEMY</h1>
  <p class="front-role">Head Pianist</p>
  <p class="front-name">Harriet Dowse</p>
  <div class="front-rule"></div>
  <div class="contact-band">
    <p class="contact-item contact-phone">
      <svg width="16" height="18" viewBox="0 0 16 18"><path d="M3 1 L6 1 L7 5 L5 6.5 Q6.5 10.5 10 12.5 L11.5 10.5 L15 12 L14.5 15.5 Q13 17 10.5 16.5 Q2 13 1 3.5 Q1.5 1.5 3 1 Z" fill="var(--accent-red)"/></svg>
      0418 769 052
    </p>
    <p class="contact-item contact-email">
      <svg width="18" height="12" viewBox="0 0 18 12"><rect width="18" height="12" fill="var(--accent-red)"/><path d="M0 0 L9 7 L18 0" fill="none" stroke="var(--band-dark)" stroke-width="1.5"/></svg>
      cadenzaelitekeys@mailbox-example.com
    </p>
    <p class="contact-item contact-web">
      <svg width="16" height="16" viewBox="0 0 16 16" fill="none" stroke="var(--accent-red)" stroke-width="1.3"><circle cx="8" cy="8" r="7"/><ellipse cx="8" cy="8" rx="3" ry="7"/><path d="M1 8 H15 M2.5 4.5 H13.5 M2.5 11.5 H13.5"/></svg>
      http://harrietdowse.sitebuilder-example.com/cadenzakeyboard
    </p>
  </div>
  <div class="front-foot"></div>
</section>

<section class="card card-back" aria-label="Business card back">
  <div class="keyboard-photo" role="img" aria-label="Photograph of two hands playing a mirrored piano keyboard"></div>
  <div class="red-rail"></div>
  <div class="name-panel-extend"></div>
  <div class="name-panel">
    <p class="brand-name"><span class="brand-square"></span>HARRIET DOWSE</p>
  </div>
  <div class="service-tab">CADENZA ELITE KEYBOARD ACADEMY</div>
  <div class="venue-photo" role="img" aria-label="Photograph of an illuminated event venue with a statue and coloured lights"></div>
  <ul class="service-list">
    <li>Individual Piano lesson</li>
    <li>Wedding Organising Band</li>
    <li>Venue Hiring</li>
    <li>Instrumental Hiring</li>
    <li>Organise Concert to Students</li>
  </ul>
</section>

</body>
</html>
```